Business Card Design

I already have a company logo for my company. I have a logo for the manufacturer we represent. I want a professional business card design.

```html
<!DOCTYPE html>
<html lang="en">
<head>
<meta charset="UTF-8">
<title>Signal Guard Services LLC — Business Card</title>
<link rel="stylesheet" href="https://fonts.googleapis.com/css2?family=Poppins:ital,wght@0,400;0,500;0,700;1,400&display=swap">
<style>
  :root {
    --canvas-bg: #e4e5ea;
    --card-white: #f4f4f4;
    --card-black: #121112;
    --brand-red: #d7111b;
    --ink: #1b1b1b;
    --ink-soft: #2a2a2a;
    --paper-shadow: rgba(0, 0, 0, 0.18);
  }
  * { box-sizing: border-box; margin: 0; padding: 0; }
  html, body {
    width: 1200px;
    height: 900px;
    overflow: hidden;
    background: var(--canvas-bg);
    font-family: "Poppins", sans-serif;
  }
  .sheet {
    width: 1200px;
    height: 900px;
    display: flex;
    flex-direction: column;
    align-items: center;
    justify-content: center;
    gap: 40px;
  }
  .card {
    width: 630px;
    height: 360px;
    border-radius: 4px;
    box-shadow: 0 10px 30px var(--paper-shadow);
    position: relative;
    overflow: hidden;
  }

  /* Front */
  .card--front {
    background: var(--card-white);
    display: flex;
    align-items: center;
  }
  .front__brand {
    width: 275px;
    display: flex;
    align-items: center;
    justify-content: center;
    gap: 10px;
    padding-left: 20px;
  }
  .brand-mark {
    width: 16px;
    height: 16px;
    border-radius: 50%;
    background: var(--brand-red);
    flex-shrink: 0;
  }
  .brand-name {
    font-weight: 700;
    font-size: 19px;
    line-height: 1.2;
    text-transform: uppercase;
    letter-spacing: 0.5px;
  }
  .front__brand .brand-name { color: var(--ink); }
  .front__divider {
    width: 2px;
    height: 240px;
    background: var(--brand-red);
    margin-right: 36px;
  }
  .front__details { display: flex; flex-direction: column; }
  .person__name {
    font-size: 26px;
    font-weight: 500;
    color: var(--ink);
    text-transform: uppercase;
    line-height: 1.1;
  }
  .person__name strong { color: var(--brand-red); font-weight: 700; }
  .person__role {
    font-style: italic;
    font-size: 17px;
    color: var(--ink);
    margin: 4px 0 0 18px;
  }
  .contact-list {
    list-style: none;
    margin: 26px 0 0 40px;
    display: flex;
    flex-direction: column;
    gap: 6px;
  }
  .contact-list li {
    display: flex;
    align-items: flex-start;
    gap: 10px;
    font-size: 15.5px;
    color: var(--ink-soft);
    line-height: 1.35;
  }
  .contact-icon {
    width: 20px;
    height: 20px;
    flex-shrink: 0;
    margin-top: 1px;
  }

  /* Back */
  .card--back {
    background: var(--card-black);
    display: flex;
    align-items: center;
    justify-content: center;
    gap: 14px;
  }
  .card--back .brand-mark { width: 22px; height: 22px; }
  .card--back .brand-name {
    color: #ffffff;
    font-size: 28px;
  }
</style>
</head>
<body>
<main class="sheet">

  <section class="card card--front" aria-label="Business card front">
    <div class="front__brand">
      <span class="brand-mark"></span>
      <span class="brand-name">Signal Guard<br>Services LLC</span>
    </div>
    <div class="front__divider"></div>
    <div class="front__details">
      <h1 class="person__name">Sample <strong>Name</strong></h1>
      <p class="person__role">Designation</p>
      <ul class="contact-list">
        <li>
          <svg class="contact-icon" viewBox="0 0 20 20" aria-hidden="true">
            <circle cx="10" cy="10" r="10" fill="var(--brand-red)"/>
            <path d="M7 5.5l1.6 2.2-1 1.1c.6 1.3 1.5 2.2 2.8 2.8l1.1-1 2.2 1.6-.9 1.6c-3.3-.2-6.5-3.4-6.7-6.7z" fill="#fff"/>
          </svg>
          <span>+00 123 456789</span>
        </li>
        <li>
          <svg class="contact-icon" viewBox="0 0 20 20" aria-hidden="true">
            <circle cx="10" cy="10" r="10" fill="var(--brand-red)"/>
            <rect x="5" y="6.5" width="10" height="7" rx="0.8" fill="#fff"/>
            <path d="M5.3 7l4.7 3.6L14.7 7" stroke="var(--brand-red)" stroke-width="1" fill="none"/>
          </svg>
          <span>email@website.com</span>
        </li>
        <li>
          <svg class="contact-icon" viewBox="0 0 20 20" aria-hidden="true">
            <circle cx="10" cy="10" r="10" fill="var(--brand-red)"/>
            <g stroke="#fff" stroke-width="1" fill="none">
              <circle cx="10" cy="10" r="5"/>
              <ellipse cx="10" cy="10" rx="2.2" ry="5"/>
              <path d="M5 10h10M6 7.5h8M6 12.5h8"/>
            </g>
          </svg>
          <span>www.website.com</span>
        </li>
        <li>
          <svg class="contact-icon" viewBox="0 0 20 20" aria-hidden="true">
            <circle cx="10" cy="10" r="10" fill="var(--brand-red)"/>
            <path d="M10 4.5a3.6 3.6 0 0 0-3.6 3.6c0 2.7 3.6 7 3.6 7s3.6-4.3 3.6-7A3.6 3.6 0 0 0 10 4.5z" fill="#fff"/>
            <circle cx="10" cy="8.1" r="1.3" fill="var(--brand-red)"/>
          </svg>
          <span>123, ABC Street, Area Name<br>City Name, Country 0000</span>
        </li>
      </ul>
    </div>
  </section>

  <section class="card card--back" aria-label="Business card back">
    <span class="brand-mark"></span>
    <span class="brand-name">Signal Guard Services LLC</span>
  </section>

</main>
</body>
</html>
```